Business card design for BrandVexa
BrandVexa
Project: Business card design for BrandVexa
Business card design for BrandVexa - Printing
Creative Brief
Professional
Dalton Wexford
Edmonton, Alberta, Canada
dalton@brandvexa.example
www.brandvexa.example
Possibly a dark background with nice effects. I am open to layer effect changes of my logo "BV". I will be changing my website banner in the future as well to make everything uniform.
Logo and web address logo can be downloaded here: https://www.filedrop.example/s/q8271n904tbpe3x/BV%20logo%20red%20and%20black.psd
brandvexa brandvexa
I like the bak of draft 44
I believe the"BV" box in the logo should be removed on the front of the cards. It just doesn't look right with the arched themed designs. I do like just the "BV" on the back of the card with url. I was hoping for more effects in the colour rather than just solid. Less red and more grey fading into lighter greys. Hopes this makes sense. Thanks for your hard work!

```html
<!DOCTYPE html>
<html lang="en">
<head>
<meta charset="utf-8">
<title>BrandVexa Business Card</title>
<link href="https://fonts.googleapis.com/css2?family=Open+Sans:wght@400;600;700&display=swap" rel="stylesheet">
<style>
  :root {
    --page-bg: #e9e6e2;
    --front-top: #9a9a9c;
    --front-mid: #d2d2d4;
    --front-bottom: #f4f4f5;
    --back-top: #8c8c8e;
    --back-mid: #5c5c5e;
    --back-bottom: #3e3e40;
    --brand-red: #e0202f;
    --text-grey: #5a5a5c;
    --contact-grey: #6a6a6c;
    --mark-area: #6e6e70;
    --white: #ffffff;
  }
  * { box-sizing: border-box; margin: 0; padding: 0; }
  html, body {
    width: 1200px; height: 1016px; overflow: hidden;
    background: var(--page-bg);
    font-family: "Open Sans", Arial, sans-serif;
  }
  .card {
    position: absolute; top: 82px;
    width: 500px; height: 900px;
    border-radius: 32px; overflow: hidden;
    box-shadow: 0 6px 18px rgba(0,0,0,0.25);
  }
  .card--front {
    left: 80px;
    background: linear-gradient(180deg, var(--front-top) 0%, var(--front-mid) 38%, var(--front-bottom) 100%);
  }
  .card--back {
    left: 640px;
    background: linear-gradient(180deg, var(--back-top) 0%, var(--back-mid) 45%, var(--back-bottom) 100%);
  }
  .brand {
    position: absolute; left: 38px; top: 150px;
  }
  .brand__name {
    font-size: 68px; font-weight: 600; color: var(--brand-red);
    letter-spacing: 1px; line-height: 1;
  }
  .person {
    position: absolute; left: 40px; top: 584px;
  }
  .person__name {
    font-size: 42px; font-weight: 600; color: var(--brand-red); line-height: 1.1;
  }
  .person__location {
    margin-top: 14px;
    font-size: 25px; font-weight: 700; color: var(--text-grey);
  }
  .contacts {
    position: absolute; left: 56px; top: 712px;
    list-style: none;
  }
  .contacts__item {
    display: flex; align-items: center; gap: 14px;
    height: 30px;
    font-size: 21px; color: var(--contact-grey);
  }
  .contacts__icon { width: 24px; height: 24px; flex: none; }
  .back-mark {
    position: absolute; left: 28px; top: 88px;
    width: 444px; height: 132px;
    background: linear-gradient(180deg, #7a7a7c 0%, var(--mark-area) 100%);
    box-shadow: inset 0 4px 8px rgba(0,0,0,0.25);
  }
  .back-band {
    position: absolute; left: 0; top: 768px;
    width: 100%; height: 48px;
    background: var(--brand-red);
    display: flex; align-items: center; justify-content: center;
    font-size: 28px; font-weight: 700; color: var(--white);
  }
</style>
</head>
<body>
  <section class="card card--front">
    <div class="brand">
      <span class="brand__name">BrandVexa</span>
    </div>
    <div class="person">
      <h1 class="person__name">Dalton Wexford</h1>
      <p class="person__location">Edmonton, Alberta, Canada</p>
    </div>
    <ul class="contacts">
      <li class="contacts__item">
        <svg class="contacts__icon" viewBox="0 0 24 24"><circle cx="12" cy="12" r="9" fill="#6a6a6c"/><path d="M3 12h18M12 3c4 4 4 14 0 18M12 3c-4 4-4 14 0 18" stroke="#d8d8da" stroke-width="1.4" fill="none"/></svg>
        1.877.555.0187
      </li>
      <li class="contacts__item">
        <svg class="contacts__icon" viewBox="0 0 24 24"><path d="M7 3l3 4-2 2c1 3 3 5 6 6l2-2 4 3-2 4C11 20 4 13 3 5z" fill="#6a6a6c"/></svg>
        780.555.0188
      </li>
      <li class="contacts__item">
        <svg class="contacts__icon" viewBox="0 0 24 24"><rect x="7" y="2" width="10" height="20" rx="2" fill="#6a6a6c"/><rect x="9" y="5" width="6" height="11" fill="#d8d8da"/></svg>
        780.555.0174
      </li>
      <li class="contacts__item">
        <svg class="contacts__icon" viewBox="0 0 24 24"><rect x="7" y="2" width="10" height="7" fill="#6a6a6c"/><rect x="2" y="9" width="20" height="10" rx="2" fill="#6a6a6c"/><rect x="6" y="15" width="12" height="7" fill="#8a8a8c"/></svg>
        780.555.0121
      </li>
      <li class="contacts__item">
        <svg class="contacts__icon" viewBox="0 0 24 24"><rect x="2" y="5" width="20" height="14" rx="2" fill="#6a6a6c"/><path d="M3 6l9 7 9-7" stroke="#d8d8da" stroke-width="1.6" fill="none"/></svg>
        dalton@brandvexa.example
      </li>
    </ul>
  </section>

  <section class="card card--back">
    <div class="back-mark" role="img" aria-label="Embossed brand monogram area"></div>
    <div class="back-band">www.brandvexa.example</div>
  </section>
</body>
</html>
```